Tavenored Crest

Need very crisp business cards for Tavenor Crest per the logo attached. The vision of Tavenor Crest is 'Steer every Venture to Tavenor'. I am going into Freelance | Consulting | Contracting and need this communicated on the card. I need the card to provide a clear message of professionalism and what the vision emulates. Will need an area for my website, LinkedIn, Twitter, as fell as the obvious Name, Address, phone, email... on the back, I would like the Vision but receptive to your design ideas.

```html
<!DOCTYPE html>
<html lang="en">
<head>
<meta charset="UTF-8">
<title>Tavenored Crest — Business Cards</title>
<link rel="stylesheet" href="https://fonts.googleapis.com/css2?family=Lato:wght@400;700;900&family=Montserrat:wght@500;600&display=swap">
<style>
  :root {
    --stage: #2b2b2d;
    --navy: #050b2a;
    --navy-edge: #0c1540;
    --brand-blue: #1d3c8f;
    --rule-blue: #1a2a78;
    --ink: #2a2a2a;
    --paper: #ffffff;
    --paper-shade: #f3f3f3;
  }
  * { margin: 0; padding: 0; box-sizing: border-box; }
  html, body {
    width: 1200px; height: 900px; overflow: hidden;
    background: var(--stage);
    font-family: "Lato", Arial, sans-serif;
  }
  .sheet {
    position: relative; width: 1200px; height: 900px;
    display: flex; flex-direction: column; align-items: center; justify-content: center; gap: 44px;
  }
  .card {
    position: relative; width: 700px; height: 400px; border-radius: 26px; overflow: hidden;
    box-shadow: 0 12px 30px rgba(0,0,0,.45);
  }
  .card--front {
    background: radial-gradient(ellipse at 60% 35%, var(--navy-edge), var(--navy) 70%);
    color: var(--paper);
  }
  .card--back {
    background: linear-gradient(180deg, var(--paper), var(--paper-shade));
    color: var(--ink);
  }
  .wordmark {
    display: flex; align-items: center; gap: 14px;
    font-family: "Montserrat", Arial, sans-serif; font-weight: 600;
    font-size: 40px; letter-spacing: -0.5px; white-space: nowrap;
  }
  .wordmark__square { width: 30px; height: 30px; flex: none; }
  .card--front .wordmark { position: absolute; left: 150px; top: 130px; color: var(--paper); }
  .card--front .wordmark__square { background: var(--paper); }
  .card--back .wordmark { position: absolute; left: 150px; top: 100px; color: var(--brand-blue); }
  .card--back .wordmark__square { background: var(--brand-blue); }
  .holder {
    position: absolute; left: 0; right: 0; top: 232px; text-align: center;
  }
  .holder__name { font-weight: 700; font-size: 20px; letter-spacing: .5px; text-transform: uppercase; }
  .holder__role { margin-top: 8px; font-size: 15px; font-weight: 700; letter-spacing: .3px; }
  .rule {
    position: absolute; left: 40px; right: 40px; top: 288px; height: 2px; background: var(--rule-blue);
  }
  .socials {
    position: absolute; right: 44px; top: 208px; text-align: right; font-size: 15px; line-height: 22px;
  }
  .socials__web { color: var(--brand-blue); font-weight: 900; }
  .contacts {
    position: absolute; left: 44px; top: 304px; font-size: 15px; line-height: 24px;
  }
  .contact { display: flex; align-items: center; gap: 10px; }
  .contact svg { width: 16px; height: 16px; fill: var(--brand-blue); flex: none; }
  .contact__address { font-weight: 900; padding-left: 26px; }
</style>
</head>
<body>
<main class="sheet">
  <section class="card card--front" aria-label="Card front">
    <div class="wordmark"><span class="wordmark__square"></span>Tavenored Crest</div>
    <div class="holder">
      <p class="holder__name">Marcus Hale</p>
      <p class="holder__role">Freelance | Consulting | Contracting</p>
    </div>
  </section>

  <section class="card card--back" aria-label="Card back">
    <div class="wordmark"><span class="wordmark__square"></span>Tavenored Crest</div>
    <div class="socials">
      <p>Netlink.com/marcus</p>
      <p>Chirpline.com/marcus</p>
      <p class="socials__web">www.tcwebsite.com</p>
    </div>
    <div class="rule"></div>
    <div class="contacts">
      <p class="contact">
        <svg viewBox="0 0 16 16" aria-hidden="true"><path d="M1 5c0-2 3-3 7-3s7 1 7 3v1.5h-3.5V5h-7v1.5H1z M4 8h8l2 6H2z"/></svg>
        250.555.0148
      </p>
      <p class="contact">
        <svg viewBox="0 0 16 16" aria-hidden="true"><path d="M1 3h14v10H1z M2.5 4.5 8 9l5.5-4.5v-.2H2.5z" fill-rule="evenodd"/></svg>
        contactmarcus@tcwebsite.com
      </p>
      <p class="contact contact__address">1480 Alder Rd, Fernhill, BC, V0X 3K2</p>
    </div>
  </section>
</main>
</body>
</html>
```